Hello my Name is Esteban Ortiz. I buy and sell vintage comic books, you can refer to my instragram page qrkp.comics to get ideas and inspiration. For the front of the card I would like my company logo QRKP Comics with a yellow and black background with the bat signal or bat emblem like on my IG page and with my info Esteban Ortiz as the Owner and address/ phone number, PO Box 218873, Bayview, FL 33000, 305-555-0182 and that I buy and sell comics & collectables . Also feel free to be open to other ideas if you want. Im not stuck on one design. For the back of the card I would like for it to say follow me on Instagram QRKP.Comics with the ig emblem. Also would like the card to be vertical if possible. Thanks

```html
<!DOCTYPE html>
<html lang="en">
<head>
<meta charset="utf-8">
<title>QRKP Comics – Business Card</title>
<link rel="stylesheet" href="https://fonts.googleapis.com/css2?family=Open+Sans:wght@400;600;700&display=swap">
<style>
  :root {
    --stage: #3b3632;
    --card: #0b0b0b;
    --yellow: #f5c518;
    --white: #f2f2f2;
    --grey: #cfcfcf;
    --silver: #c9c9c9;
  }
  * { box-sizing: border-box; margin: 0; padding: 0; }
  html, body {
    width: 1200px; height: 900px; overflow: hidden;
    background: var(--stage);
    font-family: "Open Sans", Arial, sans-serif;
  }
  .stage {
    position: relative; width: 1200px; height: 900px;
    display: flex; justify-content: center; align-items: center; gap: 40px;
  }
  .card {
    position: relative; width: 540px; height: 310px;
    background: var(--card);
    box-shadow: 0 8px 24px rgba(0,0,0,.45);
    overflow: hidden;
  }

  /* Front */
  .brand {
    position: absolute; left: 28px; top: 110px;
    display: flex; align-items: center; gap: 10px;
  }
  .brand-dot { width: 26px; height: 26px; border-radius: 50%; background: var(--yellow); flex: none; }
  .brand-name { color: var(--yellow); font-weight: 700; font-size: 25px; letter-spacing: .5px; white-space: nowrap; }
  .divider {
    position: absolute; left: 262px; top: 50px; width: 1px; height: 150px;
    background: var(--yellow); opacity: .8;
  }
  .contact { position: absolute; left: 284px; top: 56px; right: 16px; }
  .contact-name { color: var(--yellow); font-weight: 700; font-size: 20px; letter-spacing: .5px; text-transform: uppercase; white-space: nowrap; }
  .contact-role { color: var(--white); font-size: 12px; margin: 2px 0 0 12px; }
  .contact-phone {
    display: flex; align-items: center; gap: 5px;
    color: var(--white); font-size: 19px; margin: 22px 0 0 24px; white-space: nowrap;
  }
  .contact-phone svg { width: 13px; height: 13px; fill: var(--yellow); flex: none; }
  .contact-address { color: var(--grey); font-size: 12.5px; margin: 8px 0 0 42px; white-space: nowrap; }
  .tagline {
    position: absolute; left: 0; right: 0; bottom: 34px; text-align: center;
    color: var(--yellow); font-weight: 700; font-size: 17px; letter-spacing: .3px;
  }

  /* Back */
  .back-brand {
    position: absolute; left: 0; right: 0; top: 105px;
    display: flex; justify-content: center; align-items: center; gap: 10px;
  }
  .back-brand .brand-dot { background: var(--silver); }
  .back-brand .brand-name { color: var(--silver); }
  .follow {
    position: absolute; left: 0; right: 0; top: 205px;
    display: flex; justify-content: center; align-items: center; gap: 8px;
    color: var(--white); font-size: 12px;
  }
  .follow-label { font-weight: 600; text-transform: uppercase; }
  .follow-square { width: 16px; height: 16px; border-radius: 3px; background: #d6336c; }
</style>
</head>
<body>
<main class="stage">
  <section class="card card-front">
    <div class="brand">
      <span class="brand-dot"></span>
      <span class="brand-name">QRKP Comics</span>
    </div>
    <div class="divider"></div>
    <div class="contact">
      <p class="contact-name">Esteban Ortiz</p>
      <p class="contact-role">Owner</p>
      <p class="contact-phone">
        <svg viewBox="0 0 24 24" aria-hidden="true"><path d="M6.6 10.8a15.1 15.1 0 0 0 6.6 6.6l2.2-2.2a1 1 0 0 1 1-.25 11.4 11.4 0 0 0 3.6.57 1 1 0 0 1 1 1V20a1 1 0 0 1-1 1A17 17 0 0 1 3 4a1 1 0 0 1 1-1h3.5a1 1 0 0 1 1 1c0 1.25.2 2.45.57 3.57a1 1 0 0 1-.25 1z"/></svg>
        305-555-0182
      </p>
      <p class="contact-address">PO Box 218873, Bayview, FL 33000</p>
    </div>
    <p class="tagline">WE BUY AND SELL COMICS &amp; COLLECTABLES</p>
  </section>

  <section class="card card-back">
    <div class="back-brand">
      <span class="brand-dot"></span>
      <span class="brand-name">QRKP Comics</span>
    </div>
    <div class="follow">
      <span class="follow-label">Follow me on</span>
      <span class="follow-square"></span>
      <span class="follow-handle">QRKP.Comics</span>
    </div>
  </section>
</main>
</body>
</html>
```